Need simple and modern looking business card with all my information on one side and logo on the other side
Info :
Company name - VELMAR CONSTRUCTION LLC
Company addres- 418 harbor 87th. Dunmoor park ny 10352
Email- velmarllc@tridomail.Com
Company phone number 555-318-6094
Cell number- 555-742-0583
Web site - velmarllc.Com
My name Gerald tomasino

Target Market(s)

Construction , home improvement, remodeling

Industry/Entity Type

Construction

Contact Information for Business Card

It has to be moder but at the same time simple

Font styles to use
Sans Serif

Colors
0255a3
ffffff
000000
f78f20
b1b1b1
9d9d9d
1b1b1b
33a6d7
ec1f27

Requirements
Must have
• My logo on one side maybe with a some kind of background on the other side all my information
Nice to have
• Some kind of background pictures provided by you .PLEASE HAVE ACCOUNT WITH PIXELVAULT WILL NOT PAY ANY EXTRA FEES .
Should not have
• Any kind of hamer, nails,screws, helmets itp. Please do not copy the other designs come up with something new.

```html
<!DOCTYPE html>
<html lang="en">
<head>
<meta charset="utf-8">
<title>Velmar Construction LLC – Business Card</title>
<link rel="stylesheet" href="https://fonts.googleapis.com/css2?family=Arimo:wght@400;700&family=Baloo+2:wght@700&display=swap">
<style>
  :root {
    --backdrop: #d4efc2;
    --card: #ffffff;
    --ink: #1b1b1b;
    --blue: #1f77c0;
    --red: #ec1f27;
    --orange: #f78f20;
  }
  * { margin: 0; padding: 0; box-sizing: border-box; }
  html, body { width: 1200px; height: 1200px; overflow: hidden; }
  body {
    background: var(--backdrop);
    position: relative;
    font-family: "Arimo", Arial, sans-serif;
    color: var(--ink);
  }
  .card {
    position: absolute;
    width: 776px;
    height: 469px;
    background: var(--card);
  }
  .card--info { left: 20px; top: 130px; }
  .card--logo { left: 388px; top: 678px; }

  .holder-name {
    position: absolute;
    left: 40px;
    top: 6px;
    font-family: "Baloo 2", "Arial Rounded MT Bold", sans-serif;
    font-weight: 700;
    font-size: 60px;
    letter-spacing: -0.5px;
    line-height: 1.1;
  }
  .phone-line {
    position: absolute;
    left: 42px;
    font-size: 29px;
    line-height: 1;
    white-space: nowrap;
  }
  .phone-line--office { top: 91px; }
  .phone-line--mobile { top: 139px; }
  .phone-label { color: var(--blue); font-weight: 400; margin-right: 8px; }
  .phone-number { font-weight: 700; }

  .contact-list {
    position: absolute;
    left: 268px;
    top: 268px;
    list-style: none;
    font-size: 28px;
    line-height: 1;
    white-space: nowrap;
  }
  .contact-list li { height: 43px; }
  .contact-list .web { font-size: 26px; height: 40px; }
  .contact-value { font-weight: 700; }
  .label-email { color: var(--red); }
  .label-where { color: var(--orange); }

  .company-footer {
    position: absolute;
    left: 154px;
    top: 434px;
    width: 610px;
    height: 34px;
  }
  .company-footer text,
  .wordmark text {
    font-family: "Arimo", Arial, sans-serif;
    font-weight: 700;
    fill: var(--ink);
  }

  .brand-square {
    position: absolute;
    right: 22px;
    top: 70px;
    width: 70px;
    height: 70px;
    background: var(--orange);
  }
  .wordmark {
    position: absolute;
    left: 4px;
    top: 290px;
    width: 768px;
    height: 176px;
  }
</style>
</head>
<body>

  <section class="card card--info">
    <h1 class="holder-name">Gerald Tomasino</h1>
    <p class="phone-line phone-line--office"><span class="phone-label">Phone</span><span class="phone-number">555-318-6094</span></p>
    <p class="phone-line phone-line--mobile"><span class="phone-label">Mobile</span><span class="phone-number">555-742-0583</span></p>

    <ul class="contact-list">
      <li class="web">www: velmarllc.Com</li>
      <li><span class="label-email">e-mail: </span><span class="contact-value">velmarllc@tridomail.Com</span></li>
      <li><span class="label-where">where: </span><span class="contact-value">418, harbor 87th.</span></li>
      <li><span class="contact-value">Dunmoor park ny 10352</span></li>
    </ul>

    <svg class="company-footer" viewBox="0 0 610 34" aria-label="VELMAR CONSTRUCTION LLC">
      <text x="0" y="31" font-size="38" textLength="610" lengthAdjust="spacingAndGlyphs">VELMAR CONSTRUCTION LLC</text>
    </svg>
  </section>

  <section class="card card--logo">
    <div class="brand-square"></div>
    <svg class="wordmark" viewBox="0 0 768 176" aria-label="VELMAR CONSTRUCTION LLC">
      <text x="0" y="112" font-size="150" textLength="768" lengthAdjust="spacingAndGlyphs">VELMAR</text>
      <text x="0" y="172" font-size="50" textLength="768" lengthAdjust="spacingAndGlyphs">CONSTRUCTION LLC</text>
    </svg>
  </section>

</body>
</html>
```